Disability and mental health support work company requires business card

Specialising
Wrenfield Disability is a new QCAP service aimed toward QCAP participants with a history of criminal justice, psychosocial/mental health, intellectual, and cognitive disabilities.

Our focus
Focusing on providing core QCAP supports for community participation, daily activities and supported independent living.

Authentic
Likeminded people wanting to make a difference in participant's lives.

Our aim to provide holistic and empowering supports targeted towards creating independence and guidance for all participants and families.
Over 35 years of experience working with people that have psychosocial, intellectual, and cognitive disabilities.

Industry/Entity Type

disability and mental health

Contact Information for Business Card

logo - business name

Colors
0054AA
0677BA
7BADD7
CADEEF
E8F1F8
FFF300
FFF600
FEFA6F
FFFEC7
FFFEE8

Requirements
Must have
• want double sided business cards(wont let me change it)
Should not have
• any disability related pictures

```html
<!DOCTYPE html>
<html lang="en">
<head>
<meta charset="UTF-8">
<title>Wrenfield Disability – Business Card</title>
<link href="https://fonts.googleapis.com/css2?family=Montserrat:wght@500;600;700&display=swap" rel="stylesheet">
<style>
  :root {
    --page-bg: #ececec;
    --card-white: #ffffff;
    --blue-deep: #2c55a0;
    --blue-mid: #4478bb;
    --blue-light: #8aabd6;
    --yellow: #f2ee78;
    --yellow-pale: #fbf8cc;
    --pill-yellow: #f3ea3c;
    --ink: #2f5aa6;
    --navy: #0b3a5c;
  }
  * { margin: 0; padding: 0; box-sizing: border-box; }
  html, body {
    width: 1200px; height: 1200px; overflow: hidden;
    background: var(--page-bg);
    font-family: "Montserrat", sans-serif;
  }
  .card {
    position: absolute; left: 110px;
    width: 980px; height: 540px;
    background: var(--card-white);
    overflow: hidden;
    box-shadow: 0 6px 18px rgba(0,0,0,0.12);
  }
  .card--front { top: 40px; }
  .card--back { top: 620px; }
  .stripes { position: absolute; inset: 0; width: 100%; height: 100%; }
  .fill-pale { fill: var(--yellow-pale); }
  .fill-yellow { fill: var(--yellow); }
  .fill-light { fill: var(--blue-light); }
  .fill-mid { fill: var(--blue-mid); }
  .fill-deep { fill: var(--blue-deep); }

  .holder-name {
    position: absolute; left: 55px; top: 36px;
    font-size: 56px; font-weight: 700; letter-spacing: 4px;
    color: var(--ink); line-height: 1;
  }
  .holder-title {
    position: absolute; left: 58px; top: 100px;
    font-size: 27px; font-weight: 600; letter-spacing: 3px;
    color: var(--ink); line-height: 1;
  }
  .icon-pill {
    position: absolute; left: 50px; top: 150px;
    width: 72px; height: 420px;
    background: var(--pill-yellow);
    border-radius: 36px 36px 0 0;
  }
  .icon {
    position: absolute; left: 11px;
    width: 50px; height: 50px;
  }
  .contact-list { list-style: none; }
  .contact-list li {
    position: absolute; left: 160px;
    font-size: 23px; font-weight: 500; color: var(--ink);
    line-height: 1;
  }
  .brand-name {
    position: absolute;
    font-weight: 700; color: var(--navy);
    line-height: 1.1; text-align: center;
  }
  .brand-name--front { left: 390px; top: 236px; font-size: 30px; }
  .brand-name--back { left: 290px; top: 200px; width: 380px; font-size: 56px; }
</style>
</head>
<body>

<section class="card card--front" aria-label="Business card front">
  <svg class="stripes" viewBox="0 0 980 540" preserveAspectRatio="none" aria-hidden="true">
    <path class="fill-pale"   d="M600,0 Q515,270 470,540 L980,540 L980,0 Z"/>
    <path class="fill-yellow" d="M655,0 Q575,270 535,540 L980,540 L980,0 Z"/>
    <path class="fill-light"  d="M710,0 Q635,270 600,540 L980,540 L980,0 Z"/>
    <path class="fill-mid"    d="M765,0 Q695,270 665,540 L980,540 L980,0 Z"/>
    <path class="fill-deep"   d="M825,0 Q760,270 730,540 L980,540 L980,0 Z"/>
  </svg>

  <h1 class="holder-name">YOUR NAME</h1>
  <p class="holder-title">CEO / DIRECTOR</p>

  <div class="icon-pill">
    <svg class="icon" style="top:30px" viewBox="0 0 50 50" aria-hidden="true">
      <circle cx="25" cy="25" r="21" fill="none" stroke="var(--ink)" stroke-width="3"/>
      <path d="M18 15 l4 -1 l3 6 l-3 2 q2 5 6 7 l2 -3 l6 3 l-1 4 q-3 2 -7 0 q-8 -4 -11 -12 q-1 -4 1 -6 Z" fill="none" stroke="var(--ink)" stroke-width="2"/>
    </svg>
    <svg class="icon" style="top:90px" viewBox="0 0 50 50" aria-hidden="true">
      <circle cx="25" cy="25" r="21" fill="none" stroke="var(--ink)" stroke-width="3"/>
      <rect x="19" y="13" width="12" height="24" rx="2" fill="none" stroke="var(--ink)" stroke-width="2"/>
      <line x1="23" y1="33" x2="27" y2="33" stroke="var(--ink)" stroke-width="2"/>
    </svg>
    <svg class="icon" style="top:150px" viewBox="0 0 50 50" aria-hidden="true">
      <circle cx="25" cy="25" r="21" fill="none" stroke="var(--ink)" stroke-width="3"/>
      <rect x="13" y="17" width="24" height="16" fill="none" stroke="var(--ink)" stroke-width="2"/>
      <path d="M13 17 L25 27 L37 17" fill="none" stroke="var(--ink)" stroke-width="2"/>
    </svg>
    <svg class="icon" style="top:210px" viewBox="0 0 50 50" aria-hidden="true">
      <circle cx="25" cy="25" r="21" fill="none" stroke="var(--ink)" stroke-width="3"/>
      <circle cx="25" cy="25" r="12" fill="none" stroke="var(--ink)" stroke-width="2"/>
      <ellipse cx="25" cy="25" rx="5" ry="12" fill="none" stroke="var(--ink)" stroke-width="1.5"/>
      <line x1="13" y1="25" x2="37" y2="25" stroke="var(--ink)" stroke-width="1.5"/>
    </svg>
    <svg class="icon" style="top:270px" viewBox="0 0 50 50" aria-hidden="true">
      <circle cx="25" cy="25" r="21" fill="none" stroke="var(--ink)" stroke-width="3"/>
      <path d="M25 38 Q15 27 15 21 A10 10 0 0 1 35 21 Q35 27 25 38 Z" fill="var(--ink)"/>
      <circle cx="25" cy="21" r="4" fill="var(--pill-yellow)"/>
    </svg>
  </div>

  <ul class="contact-list">
    <li style="top:192px">555-333-777-55</li>
    <li style="top:252px">444-333-777-55</li>
    <li style="top:312px">your@email.com</li>
    <li style="top:372px">www.yourweb.com</li>
    <li style="top:432px">Your address</li>
  </ul>

  <p class="brand-name brand-name--front">Wrenfield<br>Disability</p>
</section>

<section class="card card--back" aria-label="Business card back">
  <svg class="stripes" viewBox="0 0 980 540" preserveAspectRatio="none" aria-hidden="true">
    <path class="fill-pale"   d="M0,0 L240,0 Q262,270 300,540 L0,540 Z"/>
    <path class="fill-yellow" d="M0,0 L195,0 Q215,270 250,540 L0,540 Z"/>
    <path class="fill-light"  d="M0,0 L145,0 Q168,270 205,540 L0,540 Z"/>
    <path class="fill-mid"    d="M0,0 L100,0 Q122,270 160,540 L0,540 Z"/>
    <path class="fill-deep"   d="M0,0 L55,0 Q75,270 110,540 L0,540 Z"/>

    <path class="fill-pale"   d="M720,0 Q665,270 640,540 L980,540 L980,0 Z"/>
    <path class="fill-yellow" d="M770,0 Q712,270 685,540 L980,540 L980,0 Z"/>
    <path class="fill-light"  d="M815,0 Q758,270 730,540 L980,540 L980,0 Z"/>
    <path class="fill-mid"    d="M860,0 Q803,270 775,540 L980,540 L980,0 Z"/>
    <path class="fill-deep"   d="M910,0 Q852,270 825,540 L980,540 L980,0 Z"/>
  </svg>

  <p class="brand-name brand-name--back">Wrenfield<br>Disability</p>
</section>

</body>
</html>
```